Biz Card for Harrowfield Property Partners - HWPP

Harrowfield Property Partners is a commercial real estate acquisitions firm. We buy commercial property and need to raise capital from investors for each deal we buy. The vibe needs to be: give us your money, we will multiply it.
Our website: www.hrwpp-example.com
Competitors are: https://velmarholdings-example.com/, https://tribanquepartners-example.com/, http://www.ostrellecapital-example.com/
Target Market(s)
High Net Worth Individuals, Bankers, Insurance Companies, Commercial Real Estate Brokers.
Industry/Entity Type
Investment Banking
Contact Information for Business Card
Name, Title, Addess, Cell#, Office#, email, website
Requirements
Must have
- use one of our logos. See website for look and feel: www.hrwpp-example.com
Nice to have
- see website: www.hrwpp-example.com

```html
<!DOCTYPE html>
<html lang="en">
<head>
<meta charset="utf-8">
<title>Harrowfield Property Partners – Business Card</title>
<link href="https://fonts.googleapis.com/css2?family=Roboto:wght@300;400;700&display=swap" rel="stylesheet">
<style>
  :root {
    --navy: #1d4a66;
    --navy-deep: #163a52;
    --white: #ffffff;
    --paper: #f7f8f9;
    --backdrop: #e4e6e8;
    --ink-soft: #9fb3c1;
  }
  * { margin: 0; padding: 0; box-sizing: border-box; }
  html, body { width: 1200px; height: 900px; overflow: hidden; }
  body {
    background: var(--backdrop);
    font-family: "Roboto", sans-serif;
    position: relative;
  }
  .card {
    position: absolute;
    left: 270px;
    width: 660px;
    height: 377px;
    overflow: hidden;
    box-shadow: 0 6px 18px rgba(0,0,0,0.18);
  }
  .card-back { top: 45px; background: var(--paper); }
  .card-front { top: 478px; background: var(--navy); }
  .card-art { position: absolute; inset: 0; width: 660px; height: 377px; }

  /* back side */
  .brand-wordmark {
    position: absolute;
    left: 40px;
    top: 148px;
    color: var(--white);
    font-weight: 400;
    font-size: 15px;
    line-height: 18px;
    letter-spacing: 4px;
    text-transform: uppercase;
  }
  .back-website {
    position: absolute;
    left: 120px;
    top: 318px;
    color: var(--navy);
    font-weight: 300;
    font-size: 20px;
    letter-spacing: 7px;
  }

  /* front side */
  .front-brand {
    position: absolute;
    right: 26px;
    top: 22px;
    display: flex;
    align-items: center;
    gap: 10px;
  }
  .front-brand .brand-dot {
    width: 40px; height: 40px; border-radius: 50%;
    background: var(--navy);
  }
  .front-brand .brand-name {
    color: var(--navy);
    font-weight: 400;
    font-size: 12px;
    line-height: 15px;
    letter-spacing: 3px;
    text-transform: uppercase;
  }
  .contact {
    position: absolute;
    left: 200px;
    top: 205px;
    color: var(--white);
    font-weight: 300;
    font-size: 14px;
    line-height: 20px;
  }
  .contact-name { font-weight: 700; letter-spacing: 0.5px; }
  .contact-title { font-weight: 300; }
  .contact-group { margin-top: 10px; }
  .contact-line { display: flex; align-items: center; gap: 8px; }
  .contact-line svg { width: 12px; height: 12px; flex: none; fill: var(--white); }
</style>
</head>
<body>

<section class="card card-back" aria-label="Business card, back">
  <svg class="card-art" viewBox="0 0 660 377" aria-hidden="true">
    <polygon points="0,160 470,30 500,90 0,300" fill="var(--navy)"/>
  </svg>
  <svg class="card-art" viewBox="0 0 660 377" role="img" aria-label="Lighthouse illustration">
    <rect x="490" y="0" width="170" height="377" fill="var(--navy)"/>
  </svg>
  <div class="brand-wordmark">Harrowfield<br>Property Partners</div>
  <div class="back-website">www.hrwpp-example.com</div>
</section>

<section class="card card-front" aria-label="Business card, front">
  <svg class="card-art" viewBox="0 0 660 377" aria-hidden="true">
    <polygon points="130,140 400,0 660,0 660,90 130,200" fill="var(--paper)"/>
    <rect x="0" y="0" width="160" height="377" fill="var(--paper)"/>
  </svg>
  <svg class="card-art" viewBox="0 0 660 377" role="img" aria-label="Lighthouse illustration">
    <rect x="30" y="120" width="120" height="257" fill="var(--navy)"/>
  </svg>

  <div class="front-brand">
    <span class="brand-dot"></span>
    <span class="brand-name">Harrowfield<br>Property Partners</span>
  </div>

  <div class="contact">
    <div><span class="contact-name">MARCUS HALE</span> | <span class="contact-title">Director</span></div>
    <div class="contact-line">
      <svg viewBox="0 0 12 12"><rect x="3" y="0.5" width="6" height="11" rx="1" fill="none" stroke="#fff" stroke-width="1.2"/></svg>
      (555) 214-0387
    </div>
    <div class="contact-group">
      <div class="contact-line">
        <svg viewBox="0 0 12 12"><rect x="0.5" y="2" width="11" height="8" rx="1"/><polyline points="1,3 6,7 11,3" fill="none" stroke="#1d4a66" stroke-width="1"/></svg>
        info@hrwpp-example.com
      </div>
      <div class="contact-line">
        <svg viewBox="0 0 12 12"><circle cx="6" cy="6" r="5.2" fill="none" stroke="#fff" stroke-width="1.2"/><ellipse cx="6" cy="6" rx="2.2" ry="5.2" fill="none" stroke="#fff" stroke-width="1"/><line x1="1" y1="6" x2="11" y2="6" stroke="#fff" stroke-width="1"/></svg>
        www.hrwpp-example.com
      </div>
    </div>
    <div class="contact-group">
      <div class="contact-line">
        <svg viewBox="0 0 12 12"><path d="M6 0.5a4 4 0 0 1 4 4c0 3-4 7-4 7s-4-4-4-7a4 4 0 0 1 4-4z"/><circle cx="6" cy="4.5" r="1.5" fill="#1d4a66"/></svg>
        48 Larkspur Ave, Suite 610, Brookhaven, FL 33000
      </div>
      <div class="contact-line">
        <svg viewBox="0 0 12 12"><path d="M2 1.5l2-0.5 1.5 3-1.3 1a7 7 0 0 0 3 3l1-1.3 3 1.5-0.5 2C6 11 1 6 2 1.5z"/></svg>
        (555) 214-0390
      </div>
    </div>
  </div>
</section>

</body>
</html>
```